Rocket business card

Modern business card design, use of color is good with clean space too.

Things to include on card:

Quote: I add fuel to your optometry practice

- Eyewear Sales
- Admin Duties
- Revenue Collection
- Leadership
- Tech Adoption
- COGS Reduction
- Product Sourcing
-Medical Growth

Dalton Vessey, CEO
Glint Harbor
Text Me! 847-302-1964
dalton@glintharbor.example

```html
<!DOCTYPE html>
<html lang="en">
<head>
<meta charset="utf-8">
<title>Glint Harbor Business Card</title>
<link rel="stylesheet" href="https://fonts.googleapis.com/css2?family=Open+Sans:wght@400;600;700&display=swap">
<style>
  :root {
    --orange: #ff6d00;
    --black: #0d0d0d;
    --white: #ffffff;
    --paper: #fbfbfb;
    --ink: #111111;
    --stage: #e9e6e2;
  }
  * { margin: 0; padding: 0; box-sizing: border-box; }
  html, body { width: 1200px; height: 800px; overflow: hidden; }
  body {
    background: var(--stage);
    font-family: "Open Sans", Arial, sans-serif;
    color: var(--ink);
    position: relative;
  }
  .card {
    position: absolute;
    top: 245px;
    width: 540px;
    height: 309px;
    background: var(--paper);
    overflow: hidden;
    box-shadow: 0 10px 28px rgba(0,0,0,0.18);
  }
  .card--back { left: 50px; }
  .card--front { left: 610px; }
  .card__shapes { position: absolute; inset: 0; width: 100%; height: 100%; }
  .card__wordmark {
    position: absolute;
    display: flex;
    align-items: center;
    gap: 10px;
    font-weight: 600;
    font-size: 28px;
    letter-spacing: 0.5px;
    white-space: nowrap;
  }
  .wordmark__dot { width: 26px; height: 26px; border-radius: 50%; }

  /* back */
  .card--back .card__wordmark { left: 28px; top: 118px; color: var(--white); }
  .card--back .wordmark__dot { background: var(--white); }
  .tagline {
    position: absolute;
    left: 192px; top: 26px;
    color: var(--white);
    font-size: 12.5px;
    font-weight: 600;
    white-space: nowrap;
  }
  .services {
    position: absolute;
    right: 40px; top: 92px;
    list-style: none;
    text-align: right;
    font-size: 15px;
    font-weight: 600;
    line-height: 24px;
  }
  .services li::after { content: "\2022"; margin-left: 8px; }

  /* front */
  .card--front .card__wordmark { left: 60px; top: 92px; color: var(--ink); }
  .card--front .wordmark__dot { background: var(--orange); }
  .contact {
    position: absolute;
    left: 48px; top: 178px;
    list-style: none;
    font-size: 15px;
    font-weight: 700;
    line-height: 26px;
  }
  .contact li { display: flex; align-items: center; gap: 8px; }
  .contact svg { width: 14px; height: 14px; }
  .name {
    position: absolute;
    right: 16px; top: 101px;
    color: var(--white);
    font-size: 23px;
    font-weight: 700;
    white-space: nowrap;
  }
  .name__role { font-size: 12px; font-weight: 600; margin-left: 4px; }
</style>
</head>
<body>

<section class="card card--back" aria-label="Card back">
  <svg class="card__shapes" viewBox="0 0 540 309" role="img" aria-label="Faint eye chart letters in concentric rings">
    <defs>
      <radialGradient id="chartGlowBack" cx="0.5" cy="0.5" r="0.5">
        <stop offset="0" stop-color="#f3e4da"/>
        <stop offset="1" stop-color="#fbfbfb" stop-opacity="0"/>
      </radialGradient>
    </defs>
    <circle cx="330" cy="190" r="150" fill="url(#chartGlowBack)" opacity="0.8"/>
  </svg>
  <svg class="card__shapes" viewBox="0 0 540 309" aria-hidden="true">
    <polygon points="0,0 380,0 170,309 0,309" fill="var(--orange)"/>
    <polygon points="180,20 488,20 470,50 180,50" fill="var(--black)"/>
    <rect x="512" y="175" width="10" height="134" fill="var(--black)"/>
  </svg>
  <div class="card__wordmark"><span class="wordmark__dot"></span>Glint Harbor</div>
  <p class="tagline">I add fuel to your optometry practice</p>
  <ul class="services">
    <li>Eyewear Sales</li>
    <li>Admin Duties</li>
    <li>Revenue Collection</li>
    <li>Leadership</li>
    <li>Tech Adoption</li>
    <li>COGS Reduction</li>
    <li>Product Sourcing</li>
    <li>Medical Growth</li>
  </ul>
</section>

<section class="card card--front" aria-label="Card front">
  <svg class="card__shapes" viewBox="0 0 540 309" role="img" aria-label="Faint eye chart letters in concentric rings">
    <defs>
      <radialGradient id="chartGlowFront" cx="0.5" cy="0.5" r="0.5">
        <stop offset="0" stop-color="#f3e4da"/>
        <stop offset="1" stop-color="#fbfbfb" stop-opacity="0"/>
      </radialGradient>
    </defs>
    <circle cx="170" cy="150" r="160" fill="url(#chartGlowFront)" opacity="0.8"/>
  </svg>
  <svg class="card__shapes" viewBox="0 0 540 309" aria-hidden="true">
    <rect x="20" y="0" width="10" height="150" fill="var(--black)"/>
    <polygon points="360,0 540,0 540,309 270,309" fill="var(--orange)"/>
    <polygon points="300,94 540,94 540,140 290,140" fill="var(--black)"/>
  </svg>
  <div class="card__wordmark"><span class="wordmark__dot"></span>Glint Harbor</div>
  <ul class="contact">
    <li>
      <svg viewBox="0 0 16 16" aria-hidden="true"><rect width="16" height="16" rx="2" fill="var(--black)"/><path d="M5 3.5c.6 0 1 1.8 1 2.2s-.9.8-.8 1.3c.3 1 1.3 2 2.3 2.3.5.1.9-.8 1.3-.8s2.2.4 2.2 1c0 1-1 2-2 2C6 11.5 4.5 8 4 6c-.3-1.2.4-2.5 1-2.5z" fill="var(--white)"/></svg>
      847-302-1964
    </li>
    <li>
      <svg viewBox="0 0 16 16" aria-hidden="true"><rect width="16" height="16" rx="2" fill="var(--black)"/><rect x="3" y="4.5" width="10" height="7" fill="var(--white)"/><path d="M3 4.5l5 4 5-4" fill="none" stroke="var(--black)" stroke-width="1"/></svg>
      dalton@glintharbor.example
    </li>
  </ul>
  <p class="name">Dalton Vessey<span class="name__role">(CEO)</span></p>
</section>

</body>
</html>
```